BRISKLE sparkling water needs new artwork! Based in Southern California

"Briskle" is a new sparkling water company based in Southern California that offers refreshing flavors (lime, cherry, & mango) with B vitamins and antioxidants.

We would like to see packaging designs for standard 12oz cans for each of the three flavors.
Our initial preference is to have individual artwork for each flavor.

Attached are examples of competitors' designs.
Updates

We are extending the deadline for the Thanksgiving Holiday. Thank you all for your contributions.

```html
<!DOCTYPE html>
<html lang="en">
<head>
<meta charset="utf-8">
<title>Briskle Sparkling Water – Can Labels</title>
<link rel="stylesheet" href="https://fonts.googleapis.com/css2?family=Montserrat:wght@700;800&display=swap">
<style>
  :root {
    --page-bg: #f4f7f7;
    --brand-dark: #1d5a57;
    --brand-teal: #2a9f98;
    --bubble-light: #ffffff;
    --bubble-blue: #d7ebf3;
    --cherry: #d8145a;
    --lime: #4aa341;
    --mango: #e9c21c;
    --mango-text: #b39a12;
    --silver-light: #e4ebf0;
    --silver-dark: #a9bcc8;
    --label-text: #ffffff;
  }
  * { box-sizing: border-box; margin: 0; padding: 0; }
  html, body {
    width: 1200px; height: 960px; overflow: hidden;
    background: var(--page-bg);
    font-family: "Montserrat", sans-serif;
  }
  .lineup {
    position: absolute; top: 200px; left: 90px;
    display: flex; gap: 60px;
  }
  .can-label {
    position: relative;
    width: 300px; height: 560px;
    overflow: hidden;
    border-radius: 6px;
    box-shadow: 0 6px 20px rgba(0,0,0,0.12);
    background: var(--bubble-light);
  }
  .bubble-field {
    position: absolute; inset: 0;
    background: radial-gradient(ellipse at 50% 30%, var(--bubble-light) 30%, var(--bubble-blue) 100%);
  }
  .brand-block {
    position: absolute; top: 140px; left: 0; right: 0;
    text-align: center;
  }
  .brand-name {
    font-weight: 800; font-size: 46px; letter-spacing: 3px;
    color: var(--brand-dark);
  }
  .brand-tagline {
    margin-top: 6px;
    font-weight: 700; font-size: 16px; letter-spacing: 2px;
    color: var(--brand-teal);
  }
  .flavor-band {
    position: absolute; left: 0; bottom: 0;
    width: 300px; height: 260px;
  }
  .benefits {
    position: absolute; top: 378px; left: 0; right: 0;
    text-align: center;
    font-weight: 700; font-size: 16px; letter-spacing: 2px; line-height: 1.3;
    color: var(--label-text);
  }
  .flavor-stripe {
    position: absolute; top: 448px; left: 0; right: 0; height: 52px;
    background: linear-gradient(90deg, var(--silver-light), #f3f6f8 40%, var(--silver-dark));
    display: flex; align-items: center; justify-content: center;
    font-weight: 800; font-size: 24px; letter-spacing: 4px;
  }
  .volume {
    position: absolute; top: 524px; left: 0; right: 0;
    text-align: center;
    font-weight: 700; font-size: 13px; letter-spacing: 2px;
    color: var(--label-text);
  }
  .cherry .flavor-band path { fill: var(--cherry); }
  .cherry .flavor-stripe { color: var(--cherry); }
  .lime .flavor-band path { fill: var(--lime); }
  .lime .flavor-stripe { color: var(--lime); }
  .mango .flavor-band path { fill: var(--mango); }
  .mango .flavor-stripe { color: var(--mango-text); }
</style>
</head>
<body>
  <main class="lineup">
    <section class="can-label cherry">
      <div class="bubble-field" role="img" aria-label="Sparkling water bubbles pattern"></div>
      <div class="brand-block">
        <div class="brand-name">BRISKLE</div>
        <div class="brand-tagline">SPARKLING WATER</div>
      </div>
      <svg class="flavor-band" viewBox="0 0 300 260" aria-hidden="true">
        <path d="M0,20 C80,110 220,110 300,0 L300,260 L0,260 Z"/>
      </svg>
      <p class="benefits">WITH B VITAMINS<br>AND ANTIOXIDANTS</p>
      <div class="flavor-stripe">CHERRY</div>
      <p class="volume">12 OZ</p>
    </section>

    <section class="can-label lime">
      <div class="bubble-field" role="img" aria-label="Sparkling water bubbles pattern"></div>
      <div class="brand-block">
        <div class="brand-name">BRISKLE</div>
        <div class="brand-tagline">SPARKLING WATER</div>
      </div>
      <svg class="flavor-band" viewBox="0 0 300 260" aria-hidden="true">
        <path d="M0,20 C80,110 220,110 300,0 L300,260 L0,260 Z"/>
      </svg>
      <p class="benefits">WITH B VITAMINS<br>AND ANTIOXIDANTS</p>
      <div class="flavor-stripe">LIME</div>
      <p class="volume">12 OZ</p>
    </section>

    <section class="can-label mango">
      <div class="bubble-field" role="img" aria-label="Sparkling water bubbles pattern"></div>
      <div class="brand-block">
        <div class="brand-name">BRISKLE</div>
        <div class="brand-tagline">SPARKLING WATER</div>
      </div>
      <svg class="flavor-band" viewBox="0 0 300 260" aria-hidden="true">
        <path d="M0,20 C80,110 220,110 300,0 L300,260 L0,260 Z"/>
      </svg>
      <p class="benefits">WITH B VITAMINS<br>AND ANTIOXIDANTS</p>
      <div class="flavor-stripe">MANGO</div>
      <p class="volume">12 OZ</p>
    </section>
  </main>
</body>
</html>
```